Stitchwell Studio

I'd like to have a website made in squarespace that is as close as possible to another website already on the internet. The website address of the website I'd like to base it on is: https://www.hemlinetailors.example.au

Target Market(s)

People looking for clothing alterations

Coding

Coded - Design and coding required

Number of Pages Required

1 page

Colors

Designer to choose colors to be used in the design.

Requirements
Must have
• Must be made in squarespace with a layout identical to this website: https://www.hemlinetailors.example.au

```html
<!DOCTYPE html>
<html lang="en">
<head>
<meta charset="utf-8">
<title>Stitchwell Studio</title>
<link href="https://fonts.googleapis.com/css2?family=Roboto+Slab:wght@500;700&family=Roboto:ital,wght@0,400;0,500;0,700;1,400&display=swap" rel="stylesheet">
<style>
:root{
  --ink:#1c1c1c;
  --body:#6b6b6b;
  --forest:#0f3530;
  --band:#1d3834;
  --soft:#f1f1f1;
  --white:#ffffff;
  --footer:#262626;
  --pin:#d93a2b;
  --gold:#f2c318;
}
*{margin:0;padding:0;box-sizing:border-box}
html,body{width:1200px;height:4109px;overflow:hidden}
body{position:relative;background:var(--white);font-family:'Roboto',sans-serif;color:var(--ink)}
.abs{position:absolute}
h2{font-family:'Roboto Slab',serif;font-weight:500;font-size:31px;text-align:center;position:absolute;left:0;width:1200px;color:var(--ink)}
.photo{position:absolute;box-shadow:0 0 0 4px #fff,0 2px 12px rgba(0,0,0,.35)}
.btn{position:absolute;background:var(--forest);color:#fff;font-size:14px;font-weight:700;border-radius:20px;padding:0 18px;height:36px;line-height:36px;text-transform:uppercase}
/* hero */
.hero{left:0;top:0;width:1200px;height:648px;background:linear-gradient(110deg,#6e5a4c 0%,#a79282 35%,#8b8178 55%,#3c3633 75%,#c9b8a8 100%)}
.topbar{left:0;top:0;width:1200px;height:102px;background:rgba(40,40,40,.55)}
.brand{left:112px;top:22px;width:110px;text-align:center;color:#fff}
.brand .dot{width:36px;height:36px;border:2px solid #fff;border-radius:50%;margin:0 auto 6px}
.brand span{font-family:'Roboto Slab',serif;font-size:13px;letter-spacing:1px;line-height:14px;display:block}
.nav{left:446px;top:36px;display:flex;gap:8px}
.nav a{color:#fff;font-size:15px;font-weight:500;text-decoration:none;padding:5px 12px;border-radius:14px}
.nav a.on{background:var(--forest)}
.hero-title{left:0;top:350px;width:1200px;text-align:center;color:#fff;font-family:'Roboto Slab',serif;font-weight:700;font-size:48px;text-shadow:0 2px 6px rgba(0,0,0,.4)}
/* features */
.feat{top:782px;width:254px;display:flex;gap:14px}
.feat .ic{width:60px;height:60px;border:2px solid #333;border-radius:50%;flex:none;display:flex;align-items:center;justify-content:center}
.feat b{display:block;font-size:17px;font-weight:500;margin:0 0 8px}
.feat p{font-size:14px;color:var(--body);line-height:21px}
/* about */
.about h3{font-family:'Roboto Slab',serif;font-weight:500;font-size:27px;line-height:33px;position:absolute}
.copy{position:absolute;font-size:15px;line-height:27.5px;color:var(--body);text-align:justify}
/* offers */
.soft{left:0;width:1200px;background:var(--soft)}
.cap{position:absolute;font-size:17px;color:#333}
/* partners */
.partner{position:absolute;top:2372px;width:185px;height:104px;background:#fff;box-shadow:0 1px 6px rgba(0,0,0,.2);display:flex;align-items:center;justify-content:center}
.partner i{width:44px;height:44px;border-radius:50%;background:#8a8a8a;display:block}
/* services */
.svc{position:absolute;top:2662px;width:236px;height:272px;background:#fff;box-shadow:0 1px 8px rgba(0,0,0,.22);text-align:center}
.svc svg{margin-top:20px}
.svc b{display:block;font-size:18px;font-weight:500;margin:8px 0 14px}
.svc p{font-size:14px;color:var(--body);line-height:21px;padding:0 16px}
.svc .btn{left:50%;transform:translateX(-50%);top:218px}
/* testimonial */
.quote-band{left:0;top:3022px;width:1200px;height:342px;background:linear-gradient(90deg,#1a302d,#25433e 50%,#1a302d)}
.quote{left:285px;top:3120px;width:630px;text-align:center;color:#fff;font-style:italic;font-size:15.5px;line-height:28px}
/* footer */
.foot{left:0;top:3935px;width:1200px;height:174px;background:var(--footer);color:#fff}
.social{display:flex;gap:9px;position:absolute;left:528px;top:76px}
.social i{width:29px;height:29px;border:1.5px solid #fff;border-radius:50%;display:block}
</style>
</head>
<body>

<div class="abs hero" role="img" aria-label="Tailor measuring a garment on a dress form in a sewing workshop"></div>
<div class="abs topbar"></div>
<div class="abs brand"><div class="dot"></div><span>STITCHWELL</span><span>STUDIO</span></div>
<nav class="abs nav">
  <a class="on">Home</a><a>Our Services</a><a>Current Offers</a><a>About Us</a><a>Contact Us</a><a>Store Locations</a>
</nav>
<div class="abs hero-title">YOUR ONE STOP WORKSHOP!</div>

<h2 style="top:724px">WHY CHOOSE US?</h2>
<div class="abs feat" style="left:108px"><div class="ic"><svg width="30" height="30" viewBox="0 0 30 30" fill="none" stroke="#333" stroke-width="2"><path d="M4 11h22l-2-6H6zM6 11v14h18V11M12 25v-7h6v7"/></svg></div><div><b>Stores</b><p>Lorem ipsum dolor sit amet, consectetur</p></div></div>
<div class="abs feat" style="left:362px"><div class="ic"><svg width="30" height="30" viewBox="0 0 30 30" fill="none" stroke="#333" stroke-width="2"><path d="M15 3l10 4v7c0 6-4 10-10 13C9 24 5 20 5 14V7z"/><path d="M10 15l4 4 6-7"/></svg></div><div><b>Guarantee</b><p>Lorem ipsum dolor sit amet, consectetur</p></div></div>
<div class="abs feat" style="left:616px"><div class="ic"><svg width="30" height="30" viewBox="0 0 30 30" fill="none" stroke="#333" stroke-width="2"><rect x="5" y="5" width="20" height="16"/><path d="M9 13l4 4 8-8M11 25h8"/></svg></div><div><b>Satisfaction</b><p>Lorem ipsum dolor sit amet, consectetur</p></div></div>
<div class="abs feat" style="left:870px"><div class="ic"><svg width="30" height="30" viewBox="0 0 30 30" fill="none" stroke="#333" stroke-width="2"><path d="M7 3h13l4 4v20H7z"/><path d="M11 11h9M11 15h9M11 19h5"/></svg></div><div><b>Certified Stylists</b><p>Lorem ipsum dolor sit amet, consectetur</p></div></div>

<section class="about">
  <div class="photo" style="left:112px;top:932px;width:460px;height:326px;background:linear-gradient(120deg,#f2ecdd,#e2d8c6 50%,#7a8a60)" role="img" aria-label="Seamstress fitting a bridal gown in a boutique"></div>
  <h3 style="left:612px;top:936px;width:470px">LOREM IPSUM DOLOR SIT AMET, ADIPISCING ELIT, SED DO</h3>
  <p class="copy" style="left:612px;top:1018px;width:468px">Sed ut perspiciatis unde omnis iste sit voluptatem accusantium doloremque laudantium, totam rem aperiam, eaque ipsa quae ab illo inventore veritatis et quasi architecto beatae vitae dicta explicabo. Nemo enim ipsam voluptatem quia voluptas sit aspernatur aut odit aut fugit, sed quia consequuntur magni dolores eos qui ratione voluptatem sequi nesciunt.</p>
  <div class="btn" style="left:612px;top:1210px">Read More</div>
  <div class="abs" style="left:960px;top:1155px;width:240px;height:140px;background:radial-gradient(ellipse at center,#e8c64a 0%,#d8853f 45%,rgba(255,255,255,0) 72%)" role="img" aria-label="Spools of thread and a tape measure"></div>
</section>

<div class="abs soft" style="top:1346px;height:420px"></div>
<h2 style="top:1382px">OUR CURRENT OFFERS</h2>
<div class="photo" style="left:114px;top:1445px;width:312px;height:240px;background:linear-gradient(120deg,#4b4444,#2a2a30 60%,#d8d4cf)" role="img" aria-label="Tailor measuring a man's suit jacket"></div>
<div class="photo" style="left:446px;top:1445px;width:310px;height:240px;background:linear-gradient(120deg,#b7a27c,#6f7a82 50%,#2f4a5a)" role="img" aria-label="Tailor working at a sewing machine"></div>
<div class="photo" style="left:776px;top:1445px;width:310px;height:240px;background:linear-gradient(140deg,#f0f0f0,#c8d2dc 40%,#3b5a86)" role="img" aria-label="Denim being hemmed on a sewing machine"></div>
<div class="cap" style="left:136px;top:1706px">15% Off* suits Alteration</div>
<div class="cap" style="left:467px;top:1706px">15% Off* suits Alteration</div>
<div class="cap" style="left:797px;top:1706px">15% Off* suits Alteration</div>

<section class="about">
  <h3 style="left:112px;top:1857px;width:480px">LOREM IPSUM DOLOR SIT AMET, ADIPISCING ELIT, SED DO</h3>
  <p class="copy" style="left:112px;top:1939px;width:468px">Sed ut perspiciatis unde omnis iste sit voluptatem accusantium doloremque laudantium, totam rem aperiam, eaque ipsa quae ab illo inventore veritatis et quasi architecto beatae vitae dicta explicabo. Nemo enim ipsam voluptatem quia voluptas sit aspernatur aut odit aut fugit, sed quia consequuntur magni dolores eos qui ratione voluptatem sequi nesciunt.</p>
  <div class="btn" style="left:112px;top:2132px">Read More</div>
  <div class="photo" style="left:630px;top:1857px;width:456px;height:322px;background:linear-gradient(110deg,#2a3550,#4a4038 50%,#7a6a55)" role="img" aria-label="Tailor adjusting the sleeve of a checked suit"></div>
  <div class="abs" style="left:0;top:2160px;width:195px;height:105px;background:radial-gradient(ellipse at center,#c4428a 0%,#3f8fc0 40%,rgba(255,255,255,0) 72%)" role="img" aria-label="Scissors and colourful thread spools"></div>
</section>

<div class="abs soft" style="top:2268px;height:257px"></div>
<h2 style="top:2310px">OUR PARTNERS</h2>
<div class="partner" style="left:112px"><i></i></div>
<div class="partner" style="left:309px"><i></i></div>
<div class="partner" style="left:507px"><i></i></div>
<div class="partner" style="left:704px"><i></i></div>
<div class="partner" style="left:902px"><i></i></div>

<h2 style="top:2602px">OUR SERVICES</h2>
<div class="svc" style="left:112px"><svg width="54" height="54" viewBox="0 0 54 54" fill="none" stroke="#333" stroke-width="2"><path d="M18 6l-10 6v36h38V12L36 6l-9 14z"/><path d="M27 20v28"/></svg><b>Suits Alteration</b><p>Sed ut perspiciatis unde omnis iste natus error sit voluptatem laudantium, totam aperiam, eaque ipsa quae ab illo</p><div class="btn">Read More</div></div>
<div class="svc" style="left:358px"><svg width="54" height="54" viewBox="0 0 54 54" fill="none" stroke="#333" stroke-width="2"><path d="M19 6l-11 8 5 8 5-3-4 27h26l-4-27 5 3 5-8-11-8c-1 5-4 7-8 7s-7-2-8-7z"/></svg><b>Dresses Alteration</b><p>Sed ut perspiciatis unde omnis iste natus error sit voluptatem laudantium, totam aperiam, eaque ipsa quae ab illo</p><div class="btn">Read More</div></div>
<div class="svc" style="left:606px"><svg width="54" height="54" viewBox="0 0 54 54" fill="none" stroke="#333" stroke-width="2"><path d="M23 4v12M31 4v12M22 16h10l2 10 8 22H12l8-22z"/></svg><b>Bridal Alteration</b><p>Sed ut perspiciatis unde omnis iste natus error sit voluptatem laudantium, totam aperiam, eaque ipsa quae ab illo</p><div class="btn">Read More</div></div>
<div class="svc" style="left:853px"><svg width="54" height="54" viewBox="0 0 54 54" fill="none" stroke="#333" stroke-width="2"><path d="M14 6h26l4 42h-12l-5-28-5 28H10z"/><path d="M14 13h26"/></svg><b>Jeans Alteration</b><p>Sed ut perspiciatis unde omnis iste natus error sit voluptatem laudantium, totam aperiam, eaque ipsa quae ab illo</p><div class="btn">Read More</div></div>

<div class="abs quote-band"></div>
<h2 style="top:3058px;color:#fff">WHAT OUR CLIENTS SAY</h2>
<div class="abs" style="left:220px;top:3118px;color:#fff;font-family:'Roboto Slab',serif;font-size:34px;font-weight:700">&ldquo;</div>
<p class="abs quote">Lorem ipsum dolor sit amet, consectetur adipiscing elit, sed do eiusmod tempor incididunt ut labore et dolore magna aliqua. Ut enim ad minim veniam, quis nostrud exercitation ullamco laboris nisi ut aliquip ex ea commodo consequat. Duis aute irure dolor in reprehenderit in voluptate velit esse cillum</p>
<div class="abs" style="left:776px;top:3212px;color:#fff;font-family:'Roboto Slab',serif;font-size:34px;font-weight:700">&rdquo;</div>
<div class="abs" style="left:0;top:3254px;width:1200px;text-align:center;color:var(--gold);font-size:18px;letter-spacing:3px">★★★★★</div>
<div class="abs" style="left:0;top:3288px;width:1200px;text-align:center;color:#fff;font-size:15px;font-weight:500">MARLA FENWICK</div>

<h2 style="top:3440px">OUR LOCATION</h2>
<p class="abs" style="left:260px;top:3492px;width:680px;text-align:center;font-size:14.5px;line-height:23px;color:#333">Lorem ipsum dolor sit amet, consectetur adipiscing elit, sed do eiusmod tempor incididunt ut labore et dolore magna aliqua. Ut enim ad minim veniam, quis nostrud exercitation</p>
<div class="abs" style="left:210px;top:3562px;width:780px;height:300px;background:radial-gradient(ellipse at 30% 45%,#cfcfcf,#f4f4f4 60%),#f7f7f7;border-radius:4px" role="img" aria-label="Dotted world map marking store locations"></div>

<footer class="abs foot">
  <div class="abs" style="left:413px;top:40px;font-size:15px;display:flex;align-items:center;gap:8px"><svg width="16" height="12" viewBox="0 0 16 12" fill="none" stroke="#fff" stroke-width="1.4"><rect x="1" y="1" width="14" height="10"/><path d="M1 1l7 6 7-6"/></svg>info@stitchwellstudio.example</div>
  <div class="abs" style="left:675px;top:41px;font-size:15px;display:flex;align-items:center;gap:8px"><svg width="13" height="13" viewBox="0 0 24 24" fill="#fff"><path d="M6.6 10.8a15 15 0 0 0 6.6 6.6l2.2-2.2a1 1 0 0 1 1-.25 11 11 0 0 0 3.6.6 1 1 0 0 1 1 1V20a1 1 0 0 1-1 1A17 17 0 0 1 3 4a1 1 0 0 1 1-1h3.5a1 1 0 0 1 1 1 11 11 0 0 0 .6 3.6 1 1 0 0 1-.25 1z"/></svg>555 010 2030</div>
  <div class="social"><i></i><i></i><i></i><i></i></div>
  <div class="abs" style="left:0;top:132px;width:1200px;text-align:center;font-size:13px">© 2019 Stitchwell Studio. All Rights Reserved</div>
</footer>

</body>
</html>
```